Thistlebrook Spirits Works needs a logo design

We need a logo design for Thistlebrook Spirits Works based in Kelowna, B.C. The product name is "Copper Lantern Vodka" in a 750 ml bottle. Mountains, rivers, sunshine or whatever you think!

Size of label: approximately 5" high x 4" wide

Target Market(s)

19 - 35 year old

Industry/Entity Type

Product

Logo Text

Copper Lantern Vodka

Logo styles of interest
Character Logo
Requirements
Must have
• Copper Lantern Vodka, 750 ml, 40 % alc./vol. Return for refund where applicable(french also) Thistlebrook Spirits Works, Kelowna, B.C. Canada V4K 7M9

```html
<!DOCTYPE html>
<html lang="en">
<head>
<meta charset="utf-8">
<title>Copper Lantern Vodka – Label</title>
<link rel="stylesheet" href="https://fonts.googleapis.com/css2?family=Bodoni+Moda:opsz,wght@6..96,900&family=Oregano:ital@1&display=swap">
<style>
  :root {
    --canvas-white: #ffffff;
    --glow-orange: #ff5a00;
    --panel-light: #f08a4e;
    --panel-mid: #e0601c;
    --panel-dark: #b83c08;
    --bevel-light: #f39a66;
    --bevel-dark: #8a2a04;
    --edge-line: #7a2603;
    --name-blue: #3a6fd8;
    --name-pale: #f4f7ff;
    --name-sky: #a9c4f2;
    --echo-brown: rgba(55, 18, 0, 0.6);
    --detail-ink: #111111;
  }
  html, body {
    margin: 0;
    padding: 0;
    overflow: hidden;
    background: var(--canvas-white);
  }
  .label-canvas {
    position: relative;
    width: 1200px;
    height: 670px;
    overflow: hidden;
    background: var(--canvas-white);
  }
  .orange-glow {
    position: absolute;
    left: 38px;
    top: 30px;
    width: 1124px;
    height: 610px;
    border-radius: 160px;
    background: var(--glow-orange);
    filter: blur(26px);
  }
  .label-panel {
    position: absolute;
    left: 147px;
    top: 135px;
    width: 917px;
    height: 399px;
    box-sizing: border-box;
    overflow: hidden;
    border: 1px solid var(--edge-line);
    background: radial-gradient(ellipse 55% 70% at 56% 42%, var(--panel-light) 0%, var(--panel-mid) 55%, var(--panel-dark) 100%);
    box-shadow: 0 2px 4px rgba(0,0,0,0.35);
  }
  .panel-bevel {
    position: absolute;
    inset: 0;
    width: 100%;
    height: 100%;
  }
  .name-line {
    position: absolute;
    margin: 0;
    font-family: "Bodoni Moda", serif;
    font-weight: 900;
    line-height: 1;
    white-space: nowrap;
    text-align: center;
  }
  .name-echo {
    color: var(--echo-brown);
    filter: blur(1.5px);
  }
  .name-echo--brand {
    left: -45px;
    top: -6px;
    width: 917px;
    font-size: 92px;
  }
  .name-echo--type {
    left: 94px;
    top: 74px;
    width: 917px;
    font-size: 196px;
  }
  .name-front {
    -webkit-background-clip: text;
    background-clip: text;
    color: transparent;
  }
  .name-front--brand {
    left: 0;
    top: 9px;
    width: 917px;
    font-size: 92px;
    background-image: linear-gradient(90deg, var(--name-blue) 8%, var(--name-pale) 38%, var(--name-pale) 62%, var(--name-sky) 80%, var(--name-blue) 95%);
  }
  .name-front--type {
    left: 0;
    top: 139px;
    width: 917px;
    font-size: 150px;
    background-image: linear-gradient(160deg, var(--name-sky) 25%, var(--name-pale) 50%, var(--name-blue) 85%);
  }
  .bottle-details {
    position: absolute;
    left: 0;
    top: 328px;
    width: 917px;
    margin: 0;
    font-family: "Oregano", cursive;
    font-style: italic;
    font-size: 38px;
    line-height: 1;
    color: var(--detail-ink);
    text-align: center;
    letter-spacing: 1px;
  }
</style>
</head>
<body>
<main class="label-canvas">
  <div class="orange-glow"></div>
  <section class="label-panel">
    <svg class="panel-bevel" viewBox="0 0 917 399" preserveAspectRatio="none" aria-hidden="true">
      <polygon points="0,0 917,0 897,20 20,20" fill="var(--bevel-light)" opacity="0.55"/>
      <polygon points="0,0 20,20 20,379 0,399" fill="var(--bevel-light)" opacity="0.35"/>
      <polygon points="917,0 917,399 897,379 897,20" fill="var(--bevel-dark)" opacity="0.45"/>
      <polygon points="0,399 917,399 897,379 20,379" fill="var(--bevel-dark)" opacity="0.55"/>
      <rect x="20" y="20" width="877" height="359" fill="none" stroke="var(--edge-line)" stroke-width="1.5" opacity="0.7"/>
    </svg>
    <p class="name-line name-echo name-echo--brand" aria-hidden="true">Copper Lantern</p>
    <p class="name-line name-echo name-echo--type" aria-hidden="true">Vodka</p>
    <h1 class="name-line name-front name-front--brand">Copper Lantern</h1>
    <p class="name-line name-front name-front--type">Vodka</p>
    <p class="bottle-details">750 ml, 40 % alc./vol</p>
  </section>
</main>
</body>
</html>
```